Raised Fingerprint Business Card Design

I need a business card design and I would like the image for the business cards to carry on to my stationary and website. My business is Forensic Consulting. I will be providing services to prosecuting and defense attorneys as well as law enforcement agencies in the areas of latent print comparison, crime scene investigations, and forensic training. I am looking for a color scheme of red, black, and silver. I would like a fingerprint that is raised and the text to be raised to some degree depending on your recommendations. with a fingerprint glass. I would like the card to include the business name, my name the deignation CLPE after it, phone number, web address, and physical address. I would like the phrase "veritas aequitas " placed discretely at the bottome of the card-subtle/not too bold.

Target Market(s)

Attorneys and law enforcement agencies

Industry/Entity Type

Business

Contact Information for Business Card

Delia Forsythe, CLPE
Brightwell Evidence Group, LLC
P.O. Box 583172 Sacramento, CA 95817
916.428.3071
www.brightwellevidencegroup.example
brightwellevidence@mailbox.example

Colors
ec1f27

Requirements
Must have
• Fingerprint and old fashioned handheld magnifying glass (Sherlock Holmes style.
• The Latin phrase listed above placed at the bottom of the front of the card discreetly.
Nice to have
• The fingerprint ridges (black lines) raised so the customer can feel it the texture.
• Raised lettering for either my name or the company name.
Should not have
• None that I can think of now.

```html
<!DOCTYPE html>
<html lang="en">
<head>
<meta charset="utf-8">
<title>Brightwell Evidence Group – Business Card</title>
<link rel="stylesheet" href="https://fonts.googleapis.com/css2?family=Ubuntu:wght@300;400&display=swap">
<style>
  :root {
    --page: #e9e6e2;
    --card-black: #0d0d0e;
    --card-glow: #2a2a2c;
    --red: #ec1f27;
    --red-deep: #a8161c;
    --silver-light: #f2f2f2;
    --silver-dark: #8c8c8c;
    --white: #ffffff;
    --grey-text: #cfcfcf;
    --print-dark: #1f1f21;
  }
  * { box-sizing: border-box; margin: 0; padding: 0; }
  html, body { width: 1200px; height: 1000px; overflow: hidden; }
  body {
    background: var(--page);
    font-family: "Ubuntu", "Trebuchet MS", sans-serif;
    position: relative;
  }
  .card {
    position: absolute;
    left: 215px;
    width: 770px;
    height: 440px;
    overflow: hidden;
    background: radial-gradient(ellipse at 45% 40%, var(--card-glow) 0%, var(--card-black) 65%);
    box-shadow: 0 6px 18px rgba(0,0,0,0.25);
  }
  .card--front { top: 40px; }
  .card--back { top: 520px; }

  /* front */
  .fingerprint-art {
    position: absolute;
    border-radius: 50% 50% 46% 54% / 58% 56% 44% 42%;
  }
  .card--front .fingerprint-art {
    right: -40px; top: -70px; width: 330px; height: 360px;
    background: radial-gradient(ellipse at 50% 45%, var(--red) 0%, var(--red-deep) 55%, rgba(120,10,15,0.2) 80%, transparent 100%);
  }
  .brand-front {
    position: absolute; left: 60px; top: 150px;
    display: flex; align-items: center; gap: 14px;
  }
  .brand-mark {
    width: 18px; height: 18px; border-radius: 50%;
    background: var(--red);
    flex: none;
  }
  .brand-name {
    font-weight: 300; font-size: 30px; line-height: 1.15;
    color: var(--white); letter-spacing: 0.5px;
  }
  .motto-tab {
    position: absolute; right: 0; top: 268px;
    display: flex; align-items: center;
  }
  .motto-bar {
    width: 150px; height: 12px;
    background: linear-gradient(90deg, var(--silver-dark), var(--silver-light));
  }
  .motto {
    background: var(--card-black);
    color: var(--grey-text);
    font-size: 15px; font-weight: 300;
    padding: 2px 14px 4px 10px;
    letter-spacing: 0.5px;
  }
  .web-line {
    position: absolute; left: 0; bottom: 54px; right: 0;
    display: flex; align-items: center; gap: 12px;
  }
  .web-bar {
    height: 12px;
    background: linear-gradient(90deg, var(--silver-dark), var(--silver-light));
  }
  .web-bar--left { width: 70px; }
  .web-bar--right { width: 160px; }
  .web {
    color: var(--white); font-size: 20px; font-weight: 300; letter-spacing: 0.5px;
  }

  /* back */
  .brand-panel {
    position: absolute; left: 70px; top: -10px; bottom: -10px; width: 230px;
    background: linear-gradient(180deg, var(--red) 0%, var(--red-deep) 100%);
    border-left: 5px solid var(--silver-light);
    border-right: 5px solid var(--silver-dark);
  }
  .brand-panel .brand-vertical {
    position: absolute; left: 50%; top: 50%;
    transform: translate(-50%, -50%) rotate(90deg);
    white-space: nowrap;
    display: flex; align-items: center; gap: 12px;
  }
  .brand-vertical .brand-mark { background: var(--white); width: 14px; height: 14px; }
  .brand-vertical .brand-name { font-size: 24px; }
  .card--back .fingerprint-art {
    right: -30px; top: -60px; width: 270px; height: 300px;
    background: radial-gradient(ellipse at 50% 45%, #2e2e31 0%, var(--print-dark) 55%, transparent 80%);
  }
  .contact {
    position: absolute; left: 360px; top: 90px;
    color: var(--white);
  }
  .person {
    font-size: 30px; font-weight: 300; color: var(--red);
    margin-bottom: 38px;
  }
  .person .credential { color: var(--white); font-size: 22px; }
  .contact-list { list-style: none; }
  .contact-item {
    display: flex; align-items: flex-start; gap: 14px;
    font-size: 19px; font-weight: 300; line-height: 1.3;
    margin-bottom: 22px;
  }
  .contact-icon { width: 26px; height: 26px; flex: none; }
</style>
</head>
<body>

<section class="card card--front" aria-label="Card front">
  <div class="fingerprint-art" role="img" aria-label="Large red fingerprint illustration"></div>
  <div class="brand-front">
    <span class="brand-mark"></span>
    <span class="brand-name">Brightwell Evidence Group, LLC</span>
  </div>
  <div class="motto-tab">
    <span class="motto-bar"></span>
    <span class="motto">veritas aequitas</span>
  </div>
  <div class="web-line">
    <span class="web-bar web-bar--left"></span>
    <span class="web">www.brightwellevidencegroup.example</span>
    <span class="web-bar web-bar--right"></span>
  </div>
</section>

<section class="card card--back" aria-label="Card back">
  <div class="fingerprint-art" role="img" aria-label="Faint dark fingerprint illustration"></div>
  <div class="brand-panel">
    <div class="brand-vertical">
      <span class="brand-mark"></span>
      <span class="brand-name">Brightwell Evidence Group, LLC</span>
    </div>
  </div>
  <div class="contact">
    <p class="person">Delia Forsythe<span class="credential">,CLPE</span></p>
    <ul class="contact-list">
      <li class="contact-item">
        <svg class="contact-icon" viewBox="0 0 26 26" aria-hidden="true">
          <circle cx="13" cy="13" r="12" fill="var(--red)"/>
          <rect x="9" y="6" width="8" height="14" rx="1.5" fill="none" stroke="#fff" stroke-width="1.6"/>
          <circle cx="13" cy="17.5" r="0.9" fill="#fff"/>
        </svg>
        <span>916.428.3071</span>
      </li>
      <li class="contact-item">
        <svg class="contact-icon" viewBox="0 0 26 26" aria-hidden="true">
          <circle cx="13" cy="13" r="12" fill="var(--red)"/>
          <rect x="6.5" y="8.5" width="13" height="9" fill="none" stroke="#fff" stroke-width="1.5"/>
          <polyline points="6.5,8.5 13,14 19.5,8.5" fill="none" stroke="#fff" stroke-width="1.5"/>
        </svg>
        <span>brightwellevidence@mailbox.example</span>
      </li>
      <li class="contact-item">
        <svg class="contact-icon" viewBox="0 0 26 26" aria-hidden="true">
          <circle cx="13" cy="13" r="12" fill="var(--red)"/>
          <path d="M13 20 C9 15 8.5 13 8.5 11 A4.5 4.5 0 0 1 17.5 11 C17.5 13 17 15 13 20 Z" fill="#fff"/>
          <circle cx="13" cy="11" r="1.7" fill="var(--red)"/>
        </svg>
        <span>P.O. Box 583172 Sacramento,<br>CA 95817</span>
      </li>
    </ul>
  </div>
</section>

</body>
</html>
```